"Word Cloud" lists of countries, by decade, who have adopted women's suffrage

The winning designer will (eventually, but not necessarily within this project--see "Nice to Haves", below) design a total of eight images, based on the eight lists of countries (see attached files) in order, by decade, that they adopted women's suffrage.

One of the the attached images is a screen shot of five pages of the book RISE: The Plea for The Union of Skyward, showing how these lists are presently arranged on 6"x9" pages.

We essentially want to spice up these 8 lists and make them more fun to look at, for the reader.

Target Market(s)

General audience. People who want to make a difference. People who want to do something to change the world, and want to read a book about how we can actually do it.

Industry/Entity Type

Political

Font styles to use
Serif
Sans Serif
Decorative
Script

Requirements
Must have
• At least two initial designs, one for each of the two largest lists (lists 5 and 6). All country names must be spelled correctly. A WORD doc has been provided with all the text you need to work with. An EXAMPLE word cloud has been provided for inspiration. The look and feel of these "Country Clouds" wants to go all over the place, but all names should be (at least somewhat) readable.
• IMPORTANT ELEMENTS: (1) There are a few places where current countries were just one, when they got women's suffrage. Keep this info intact, together, in the cloud. EXAMPLE (from list 6):
•  British Leeward Islands (remove ", including today’s:", but keep together with)
•  Antigua and Barbuda
•  British Virgin Islands
•  Montserrat
•  Saint Kitts and Nevis
•  Anguilla
• (2) The names of the countries should stay in roughly the same order as found in the lists, but laid out (very) roughly right to left and then top to bottom, loosely akin to the standard flow of text written in the latin alphabet. It is fine to alter this standard in minor ways to achieve a better look to the design. Just don't move a country found at the top of one list into the middle of that list or down to the bottom, etc.
• These country clouds will be printed in black and white, so keep the designs greyscale.
• These "country clouds" should be 4.5" in width.The largest country clouds, with the most countries found in them, should not exceed 6" in length.
Nice to have
• (Eventually) all 8 lists in the form of "Country Clouds"---that are playful, but with serious elements. Pull up a list of countries by population, have the 20 biggest use the biggest font sizes. Use many different fonts, mix it up! Essentially, these 8 lists all want to become word clouds, with each nation's full name as its own "word." See example cloud.
• Though having all 8 lists in clouds at the end of this project is "nice to have," the winner for this design might simply produce 2 such clouds, along with a cost estimate attached to the submitted design for what they would charge to complete the other 6 clouds.
Should not have
• Do NOT include the textual transitions found between the lists, in the screen shot or word doc. They are there just to help you see how the different graphics will be used and what will go either before or after them.
• No need to use bullet points.

```html
<!DOCTYPE html>
<html lang="en">
<head>
<meta charset="utf-8">
<title>Country Cloud</title>
<link rel="stylesheet" href="https://fonts.googleapis.com/css2?family=Arvo:wght@700&family=Cinzel:wght@500&family=Oswald:wght@500&family=Lobster+Two:ital,wght@1,700&family=Stardos+Stencil:wght@700&family=Libre+Baskerville:wght@700&family=Yellowtail&family=Audiowide&family=Poiret+One&family=Archivo+Black&family=Cormorant+Garamond:wght@400&family=Playfair+Display:wght@500&family=Spectral:wght@300&family=IM+Fell+Double+Pica+SC&family=Roboto+Condensed:wght@700&family=Marcellus&family=Montserrat:wght@700&display=swap">
<style>
  :root {
    --paper-center: #ffffff;
    --paper-edge: #e4e4e4;
    --ink-dark: #444444;
    --ink-mid: #5a5a5a;
    --ink-soft: #7c7c7c;
    --ink-light: #9a9a9a;
    --ink-pale: #adadad;
    --rule: #9c9c9c;
  }
  html, body {
    margin: 0;
    padding: 0;
    overflow: hidden;
  }
  .canvas {
    width: 985px;
    height: 1200px;
    background: radial-gradient(ellipse at 50% 55%, var(--paper-center) 0%, #f4f4f4 45%, var(--paper-edge) 100%);
    position: relative;
    overflow: hidden;
  }
  .cloud { position: absolute; inset: 0; }
  .country { dominant-baseline: alphabetic; }
  .albania { font-family: "Arvo", serif; font-weight: 700; fill: var(--ink-mid); }
  .czechoslovakia { font-family: "Cinzel", serif; font-weight: 500; fill: var(--ink-light); }
  .slovakia { font-family: "Oswald", sans-serif; font-weight: 500; fill: var(--ink-mid); }
  .czech-republic { font-family: "Lobster Two", cursive; font-style: italic; font-weight: 700; fill: var(--ink-pale); }
  .united-states { font-family: "Stardos Stencil", serif; font-weight: 700; fill: var(--ink-dark); }
  .sweden { font-family: "Libre Baskerville", serif; font-weight: 700; fill: var(--ink-pale); }
  .burma { font-family: "Yellowtail", cursive; fill: var(--ink-soft); }
  .kazakhstan { font-family: "Audiowide", sans-serif; fill: var(--ink-light); }
  .mongolia { font-family: "Poiret One", sans-serif; fill: var(--ink-soft); }
  .tajikistan { font-family: "Archivo Black", sans-serif; fill: var(--ink-mid); }
  .turkmenistan { font-family: "Cormorant Garamond", serif; font-weight: 400; fill: var(--ink-soft); }
  .italy { font-family: "Playfair Display", serif; font-weight: 500; fill: var(--ink-dark); }
  .trinidad { font-family: "Spectral", serif; font-weight: 300; fill: var(--ink-light); }
  .equador { font-family: "IM Fell Double Pica SC", serif; fill: var(--ink-soft); }
  .moldova { font-family: "Roboto Condensed", sans-serif; font-weight: 700; fill: var(--ink-mid); }
  .puerto-rico { font-family: "Marcellus", serif; fill: var(--ink-soft); }
  .romania { font-family: "Montserrat", sans-serif; font-weight: 700; fill: var(--ink-mid); }
  .split-frame { fill: none; stroke: var(--rule); stroke-width: 1.2; }
</style>
</head>
<body>
<main class="canvas">
  <svg class="cloud" width="985" height="1200" viewBox="0 0 985 1200" xmlns="http://www.w3.org/2000/svg">
    <text class="country albania" x="222" y="154" font-size="31" textLength="564" lengthAdjust="spacingAndGlyphs">THE PRINCIPALITY OF ALBANIA</text>

    <g class="split-group">
      <path class="split-frame" d="M202 204 V158 H804 V204 H828 V264 H178 V204 Z"/>
      <path class="split-frame" d="M206 204 V162 H800 V204"/>
      <text class="country czechoslovakia" x="220" y="202" font-size="46" textLength="572" lengthAdjust="spacingAndGlyphs">CZECHOSLOVAKIA</text>
      <text class="country slovakia" x="188" y="260" font-size="58" textLength="284" lengthAdjust="spacingAndGlyphs">SLOVAKIA</text>
      <text class="country czech-republic" x="480" y="258" font-size="48" textLength="340" lengthAdjust="spacingAndGlyphs">Czech Republic</text>
    </g>

    <text class="country united-states" x="174" y="336" font-size="76" textLength="658" lengthAdjust="spacingAndGlyphs">UNITED STATES</text>

    <text class="country sweden" x="172" y="416" font-size="82" textLength="436" lengthAdjust="spacingAndGlyphs">SWEDEN</text>
    <text class="country burma" x="610" y="418" font-size="70" textLength="226" lengthAdjust="spacingAndGlyphs">Burma</text>

    <text class="country kazakhstan" x="174" y="484" font-size="66" textLength="600" lengthAdjust="spacingAndGlyphs">KAZAKHSTAN</text>

    <text class="country mongolia" x="0" y="0" font-size="58" textLength="352" lengthAdjust="spacingAndGlyphs" transform="translate(790 448) rotate(90)">MONGOLIA</text>

    <text class="country tajikistan" x="166" y="564" font-size="84" textLength="608" lengthAdjust="spacingAndGlyphs">TAJIKISTAN</text>

    <text class="country turkmenistan" x="172" y="636" font-size="86" textLength="608" lengthAdjust="spacingAndGlyphs">TURKMENISTAN</text>

    <text class="country italy" x="178" y="788" font-size="190" textLength="592" lengthAdjust="spacingAndGlyphs">ITALY</text>

    <text class="country trinidad" x="164" y="844" font-size="52" textLength="668" lengthAdjust="spacingAndGlyphs">TRINIDAD AND TOBAGO</text>

    <text class="country equador" x="168" y="916" font-size="78" textLength="460" lengthAdjust="spacingAndGlyphs">EQUADOR</text>
    <text class="country moldova" x="636" y="916" font-size="48" textLength="188" lengthAdjust="spacingAndGlyphs">MOLDOVA</text>

    <text class="country puerto-rico" x="168" y="996" font-size="84" textLength="616" lengthAdjust="spacingAndGlyphs">PUERTO RICO</text>

    <text class="country romania" x="172" y="1052" font-size="48" textLength="232" lengthAdjust="spacingAndGlyphs">ROMANIA</text>
  </svg>
</main>
</body>
</html>
```